Riverpeak Analytics needs new design business card

We are video surveillance and analytics software development company.
I am looking for a professional business card.
Our website is www.riverpeakanalytics.example.au
Please have a loo and get the feel for who we are and what we do.
I do not know what else to give you apart from good luck and I hope your design gets selected.
Thank you very much for participating
Business
Contact Information for Business Card
Address
27/15 Marlowe Street Fernbrook NSW 2199
Telephone 1300 582 417
Mobile 0450 731 258
email: marcus@riverpeakanalytics.example.au
name
Marcus Helvard
Position
Managing Director
Font styles to use
Other font styles liked:
- Arial
Look and feel

```html
<!DOCTYPE html>
<html lang="en">
<head>
<meta charset="utf-8">
<title>Riverpeak Analytics – Business Card</title>
<link rel="stylesheet" href="https://fonts.googleapis.com/css2?family=Alegreya:wght@400;500&display=swap">
<style>
  :root {
    --backdrop: #d8d5cf;
    --card: #0b0b0c;
    --brand-blue: #2f5f94;
    --muted-blue: #3d6a9c;
    --text-grey: #7e8a95;
    --shadow: rgba(0, 0, 0, 0.28);
  }
  * { margin: 0; padding: 0; box-sizing: border-box; }
  html, body {
    width: 1200px;
    height: 900px;
    overflow: hidden;
    background: var(--backdrop);
    font-family: "Alegreya", Georgia, serif;
  }
  .stage {
    position: relative;
    width: 1200px;
    height: 900px;
  }
  .card {
    position: absolute;
    width: 560px;
    height: 342px;
    background: var(--card);
    box-shadow: 0 14px 30px var(--shadow);
  }
  .card--front { left: 110px; top: 130px; }
  .card--back  { left: 530px; top: 428px; }

  .wordmark {
    position: absolute;
    display: flex;
    align-items: center;
    gap: 14px;
    color: var(--brand-blue);
    font-weight: 500;
    white-space: nowrap;
  }
  .wordmark__square {
    background: var(--brand-blue);
    flex: none;
  }
  .card--front .wordmark {
    left: 50%;
    top: 50%;
    transform: translate(-50%, -50%);
    font-size: 40px;
    letter-spacing: 0.5px;
  }
  .card--front .wordmark__square { width: 40px; height: 40px; }

  .card--back .wordmark {
    right: 34px;
    top: 48px;
    font-size: 30px;
  }
  .card--back .wordmark__square { width: 30px; height: 30px; }

  .contact {
    position: absolute;
    left: 40px;
    top: 178px;
    color: var(--text-grey);
  }
  .contact__name {
    color: var(--muted-blue);
    font-size: 25px;
    font-weight: 400;
    line-height: 1.1;
  }
  .contact__role {
    font-size: 15px;
    margin-bottom: 30px;
  }
  .contact__line {
    font-size: 14.5px;
    line-height: 1.45;
  }
  .contact__label { color: var(--muted-blue); }
</style>
</head>
<body>
  <main class="stage">
    <section class="card card--front" aria-label="Business card front">
      <div class="wordmark">
        <span class="wordmark__square"></span>
        <span class="wordmark__name">Riverpeak Analytics</span>
      </div>
    </section>

    <section class="card card--back" aria-label="Business card back">
      <div class="wordmark">
        <span class="wordmark__square"></span>
        <span class="wordmark__name">Riverpeak Analytics</span>
      </div>
      <div class="contact">
        <h1 class="contact__name">Marcus Helvard</h1>
        <p class="contact__role">Position Managing Director</p>
        <p class="contact__line">Address 27/15 Marlowe Street Fernbrook NSW 2199</p>
        <p class="contact__line"><span class="contact__label">T:</span> 1300 582 417 <span class="contact__label">M:</span> 0450 731 258</p>
        <p class="contact__line"><span class="contact__label">E:</span> marcus@riverpeakanalytics.example.au</p>
      </div>
    </section>
  </main>
</body>
</html>
```